Brandlark CEO needs a Crowdsourced Graphic for a Gizmoreel Article

I need a simple graphic / banner for a blog post that's going to be posted on Gizmoreel (www.gizmoreel.example) - the biggest tech blog in the world.

The article will be written by Omar Feltz (Brandlark's CEO) and the title will be "The Quiet Harbor Surge Unveiled". The article is about the tens of thousands of people using crowdsourcing websites (like Brandlark.example, Qtaskly.example and Wervo.example) in China, India, the Philippines, Australia and other countries in the Asia Pacific region.

We'd really like to get this ASAP - so early submissions encouraged. We will try and get the winning designer linked to from the article.
Updates

Thanks to everyone that submitted!  Some great designs and hard to choose! :)

Target Market(s)

Tech saavy readers, English speakers

Industry/Entity Type

Tech

Requirements
Must have
• The graphic SHOULD:
1) Have the text "The quiet harbor surge unveiled" with some nice design and fonts (consider grey subtle pattern background and white drop shadow on fonts) - see attached examples
2) Have an Asian theme
3) Have the dimensions 640px wide by 240px wide
Nice to have
• The graphic COULD:
1) Have references to some or all of the countries mentioned above or use Asian characters as part of the background / motif (maybe the word "crowd" or "crowd sourcing" in different languages). In Chinese, the word for crowdsourcing is "witkey" (and there are corresponding Chinese characters: ??)
2) Emphasize the word "Asia" (using color and larger/different font)
3) Use a chart showing exponential (i.e. fast) growth - like the attached
4) Have a second line of text "7 Odd Facts Hiding Behind the Quiet Harbor Surge"

```html
<!DOCTYPE html>
<html lang="en">
<head>
<meta charset="utf-8">
<title>The Quiet Harbor Surge Unveiled – Banner</title>
<link rel="stylesheet" href="https://fonts.googleapis.com/css2?family=Lilita+One&family=Walter+Turncoat&display=swap">
<style>
  :root {
    --paper: #ededed;
    --paper-edge: #e2e2e2;
    --title-red: #d1232a;
    --title-glow: #ffffff;
    --band: #3e4547;
    --band-text: #f4f4f4;
    --bar-fill: #fbfbfb;
    --bar-stroke: #6f6f6f;
    --arrow: #5b5b5b;
    --globe-light: #f3f4f3;
    --globe-mid: #c9cccb;
    --globe-land: #2f7d3a;
  }
  html, body {
    margin: 0;
    padding: 0;
    overflow: hidden;
  }
  body {
    width: 1200px;
    height: 450px;
    background: var(--paper);
  }
  .banner {
    position: relative;
    width: 1200px;
    height: 450px;
    overflow: hidden;
    background: radial-gradient(ellipse at 40% 40%, var(--paper) 0%, var(--paper-edge) 100%);
  }
  .growth-chart {
    position: absolute;
    left: 0;
    top: 0;
  }
  .globe {
    position: absolute;
    left: 830px;
    top: -30px;
    width: 420px;
    height: 420px;
    border-radius: 50%;
    background:
      radial-gradient(ellipse 55% 45% at 58% 40%, var(--globe-land) 0%, var(--globe-land) 55%, rgba(47,125,58,0) 72%),
      radial-gradient(circle at 35% 35%, var(--globe-light) 0%, var(--globe-mid) 100%);
    box-shadow: inset -12px -10px 30px rgba(0,0,0,0.12);
  }
  .headline {
    position: absolute;
    left: 60px;
    top: 58px;
    margin: 0;
    font-family: "Lilita One", sans-serif;
    font-weight: 400;
    color: var(--title-red);
    text-transform: uppercase;
    line-height: 1;
    text-shadow: 2px 2px 0 var(--title-glow);
  }
  .headline .line {
    display: block;
  }
  .headline .lead {
    font-size: 92px;
    letter-spacing: 1px;
  }
  .headline .aside {
    font-size: 50px;
    letter-spacing: 2px;
  }
  .headline .line-two {
    margin-top: 8px;
    font-size: 52px;
    letter-spacing: 3px;
  }
  .info-band {
    position: absolute;
    left: 0;
    top: 328px;
    width: 1200px;
    height: 122px;
    background: var(--band);
    display: flex;
    align-items: center;
    justify-content: center;
  }
  .info-band p {
    margin: 0;
    font-family: "Walter Turncoat", cursive;
    font-size: 33px;
    letter-spacing: 3px;
    color: var(--band-text);
    text-transform: uppercase;
    white-space: nowrap;
  }
</style>
</head>
<body>
  <main class="banner">
    <div class="globe" role="img" aria-label="Globe centred on Asia, with the continent shaded green"></div>

    <svg class="growth-chart" width="1200" height="450" viewBox="0 0 1200 450" aria-hidden="true">
      <defs>
        <linearGradient id="barFade" x1="0" y1="0" x2="1" y2="0">
          <stop offset="0" stop-color="var(--bar-stroke)" stop-opacity="0.35"/>
          <stop offset="1" stop-color="var(--bar-stroke)" stop-opacity="1"/>
        </linearGradient>
      </defs>
      <g class="bars" fill="var(--bar-fill)" stroke="url(#barFade)" stroke-width="3">
        <rect x="562" y="278" width="28" height="52"/>
        <rect x="620" y="258" width="32" height="72"/>
        <rect x="681" y="225" width="32" height="105"/>
        <rect x="741" y="188" width="32" height="142"/>
        <rect x="797" y="150" width="30" height="180"/>
      </g>
      <path class="trend" d="M470 262 C 610 210, 720 170, 805 88" fill="none" stroke="var(--arrow)" stroke-width="7" stroke-linecap="round"/>
      <path class="trend-head" d="M826 64 L 790 80 L 812 102 Z" fill="var(--arrow)"/>
    </svg>

    <h1 class="headline">
      <span class="line"><span class="lead">The Quiet</span> <span class="aside">Harbor</span></span>
      <span class="line line-two">Surge Unveiled</span>
    </h1>

    <div class="info-band">
      <p>7 Odd Facts Hiding Behind the Quiet Harbor Surge</p>
    </div>
  </main>
</body>
</html>
```